Evergrove Yard Service and Beyond LLC

• Mowing
• Weed eating
•Edging
• hedge trimming
• landscaping
•mulching
•yard clean up
• pressure washing

Target Market(s)

Everyone

Contact Information for Business Card

Licensed and insured

Font styles to use
Serif

Colors
59FF00
82FF00
B8FF75
E3FFCB
F4FFEA
F0912C
F2A743
F7CA91
FBE8D2
FDF5EE
EE7325
F08F49
F5BC92
FAE3D3
FDF4ED
EB3D1F
EC4F4E
F09395
F8D3D4
FCEDEE
E54698
E96AAD
F1A4CE
F9D9EA
FCEFF6

```html
<!DOCTYPE html>
<html lang="en">
<head>
<meta charset="utf-8">
<title>Evergrove Yard Service and Beyond LLC – Business Card</title>
<link rel="stylesheet" href="https://fonts.googleapis.com/css2?family=Montserrat:wght@500;600;700&family=Mulish:wght@400;600;700&display=swap">
<style>
  :root {
    --backdrop: #cccccc;
    --card: #ffffff;
    --orange: #f58634;
    --green: #99cc33;
    --ink: #111111;
    --ink-soft: #3d3d3d;
  }
  * { margin: 0; padding: 0; box-sizing: border-box; }
  html, body { width: 1000px; height: 1200px; overflow: hidden; background: var(--backdrop); }
  .canvas { position: relative; width: 1000px; height: 1200px; }
  .card {
    position: absolute; left: 51px; width: 898px; height: 539px;
    background: var(--card); overflow: hidden;
  }
  .card--front { top: 44px; }
  .card--back { top: 617px; }
  .card__waves { position: absolute; inset: 0; width: 100%; height: 100%; }
  .wave--orange { fill: var(--orange); }
  .wave--green { fill: var(--green); }

  .brand { position: absolute; left: 67px; top: 142px; width: 380px; text-align: center; }
  .brand__dot {
    display: block; width: 150px; height: 150px; margin: 0 auto 40px;
    border-radius: 50%; background: var(--orange);
  }
  .brand__name, .brand__tagline {
    font-family: "Montserrat", sans-serif; font-weight: 600; color: var(--ink-soft);
    line-height: 1; white-space: nowrap;
  }
  .brand__name { font-size: 45px; letter-spacing: 0.02em; }
  .brand__tagline { font-size: 18.5px; margin-top: 7px; letter-spacing: 0.04em; }

  .contact { position: absolute; left: 529px; top: 152px; font-family: "Mulish", sans-serif; color: var(--ink-soft); white-space: nowrap; }
  .contact__name { font-size: 29px; font-weight: 700; line-height: 35px; }
  .contact__role { font-size: 28px; line-height: 35px; margin-bottom: 8px; }
  .contact__list { list-style: none; }
  .contact__item { display: flex; align-items: center; height: 40px; font-size: 26px; }
  .contact__icon {
    width: 25px; height: 25px; border-radius: 3px; background: var(--orange);
    margin-right: 10px; flex: none; display: flex; align-items: center; justify-content: center;
  }
  .contact__icon svg { width: 17px; height: 17px; fill: none; stroke: #fff; stroke-width: 1.8; stroke-linecap: round; stroke-linejoin: round; }

  .services {
    position: absolute; left: 67px; top: 148px; width: 800px;
    display: grid; grid-template-columns: 418px 1fr; grid-auto-flow: column; grid-template-rows: repeat(4, 53px);
    list-style: none; font-family: "Montserrat", sans-serif; font-weight: 600; font-size: 36px; color: var(--ink);
  }
  .services__item { display: flex; align-items: center; white-space: nowrap; }
  .services__item::before {
    content: ""; width: 12px; height: 12px; border-radius: 50%; background: var(--green);
    margin-right: 14px; margin-top: -8px; flex: none;
  }
  .credential {
    position: absolute; left: 457px; top: 451px; white-space: nowrap;
    font-family: "Montserrat", sans-serif; font-weight: 500; font-size: 28px; color: var(--ink); letter-spacing: 0.01em;
  }
</style>
</head>
<body>
<div class="canvas">

  <section class="card card--front">
    <svg class="card__waves" viewBox="0 0 1062 636" preserveAspectRatio="none" aria-hidden="true">
      <path class="wave--orange" d="M0,0 H1062 V76 C990,52 910,25 810,28 C620,38 360,105 200,100 C120,97 55,92 0,78 Z"/>
      <path class="wave--green" d="M0,561 C100,595 250,614 350,610 C550,602 750,540 880,537 C950,536 1010,548 1062,562 V636 H0 Z"/>
    </svg>

    <div class="brand">
      <span class="brand__dot"></span>
      <div class="brand__name">EVERGROVE</div>
      <div class="brand__tagline">YARD SERVICE AND BEYOND LLC</div>
    </div>

    <div class="contact">
      <div class="contact__name">Your Name</div>
      <div class="contact__role">Manager</div>
      <ul class="contact__list">
        <li class="contact__item"><span class="contact__icon"><svg viewBox="0 0 24 24"><path d="M6 3h3l2 5-2.5 1.5a11 11 0 0 0 6 6L16 13l5 2v3a2 2 0 0 1-2 2A16 16 0 0 1 4 5a2 2 0 0 1 2-2z"/></svg></span>123 444 555</li>
        <li class="contact__item"><span class="contact__icon"><svg viewBox="0 0 24 24"><path d="M12 21s-6-6.5-6-11a6 6 0 0 1 12 0c0 4.5-6 11-6 11z"/><circle cx="12" cy="10" r="2.2"/></svg></span>789 Your Street Here</li>
        <li class="contact__item"><span class="contact__icon"><svg viewBox="0 0 24 24"><rect x="3" y="5" width="18" height="14" rx="1"/><path d="M3 6l9 7 9-7"/></svg></span>info@yourname.com</li>
        <li class="contact__item"><span class="contact__icon"><svg viewBox="0 0 24 24"><circle cx="12" cy="12" r="9"/><path d="M3 12h18M12 3c3 3 3 15 0 18M12 3c-3 3-3 15 0 18"/></svg></span>www.yourname.com</li>
      </ul>
    </div>
  </section>

  <section class="card card--back">
    <svg class="card__waves" viewBox="0 0 1062 636" preserveAspectRatio="none" aria-hidden="true">
      <path class="wave--orange" d="M0,0 H1062 V78 C1020,95 960,102 880,98 C700,90 500,25 300,25 C180,25 80,50 0,76 Z"/>
      <path class="wave--green" d="M0,561 C60,545 120,535 200,537 C400,545 600,610 800,611 C900,611 1000,585 1062,561 V636 H0 Z"/>
    </svg>

    <ul class="services">
      <li class="services__item">Mowing</li>
      <li class="services__item">Weed eating</li>
      <li class="services__item">Edging</li>
      <li class="services__item">Hedge trimming</li>
      <li class="services__item">Landscaping</li>
      <li class="services__item">Mulching</li>
      <li class="services__item">Yard clean up</li>
      <li class="services__item">Pressure washing</li>
    </ul>

    <div class="credential">LICENSED AND INSURED</div>
  </section>

</div>
</body>
</html>
```